Harborline Stay Collective Business Card Design

Design a business card for Harborline Stay Collective. Look at the website for colors and reference. Card should have logo, name, title, office number, mobile number, email, URL and a tagline like, "Luxury Hotel & Resort Email Marketing" (This might change).

https://www.harborlinestaycollective.net

The rest I will leave up to your imagination.

Contact Information for Business Card

Logo, name, title, office number, mobile number, email, URL and a tagline like, "Luxury Hotel & Resort Email Marketing" (This might change).

```html
<!DOCTYPE html>
<html lang="en">
<head>
<meta charset="utf-8">
<title>Harborline Stay Collective – Business Card</title>
<link href="https://fonts.googleapis.com/css2?family=Montserrat:wght@400;600;700&display=swap" rel="stylesheet">
<style>
  :root {
    --bg: #d3d6d7;
    --paper: #fbfbfa;
    --orange: #e86c12;
    --orange-deep: #d95f0c;
    --ink: #3a3a3a;
    --logo-ink: #1c1c1c;
    --white: #ffffff;
  }
  * { box-sizing: border-box; margin: 0; padding: 0; }
  html, body { width: 1200px; height: 829px; overflow: hidden; }
  body {
    background: var(--bg);
    font-family: "Montserrat", sans-serif;
    position: relative;
  }
  .card {
    position: absolute;
    top: 265px;
    width: 525px;
    height: 300px;
    box-shadow: 0 14px 30px rgba(0,0,0,.18);
  }
  .card--front { left: 50px; background: var(--paper); border-bottom: 3px solid var(--orange); }
  .card--back { left: 625px; background: var(--orange); border-bottom: 3px solid var(--orange-deep); }

  .name-band {
    position: absolute;
    left: 0; top: 38px;
    width: 330px; height: 50px;
    background: var(--orange);
    display: flex; align-items: center;
    padding-left: 30px;
  }
  .name-band__name {
    color: var(--white);
    font-weight: 700;
    font-size: 22px;
    letter-spacing: 1.5px;
    text-transform: uppercase;
  }
  .brand {
    position: absolute;
    left: 345px; top: 44px;
    width: 165px;
    color: var(--logo-ink);
    font-weight: 700;
    font-size: 17px;
    line-height: 1.1;
    letter-spacing: .5px;
    text-transform: uppercase;
  }
  .contact {
    position: absolute;
    left: 30px; top: 115px;
    color: var(--ink);
    font-size: 12.5px;
    line-height: 1.45;
  }
  .contact__address { margin-bottom: 12px; }
  .contact__list { list-style: none; }
  .contact__item { display: flex; align-items: center; gap: 8px; }
  .contact__icon { width: 11px; height: 11px; flex: none; }

  .back-brand {
    position: absolute;
    left: 0; right: 0; top: 105px;
    text-align: center;
    color: var(--white);
    font-weight: 700;
    font-size: 30px;
    letter-spacing: 2px;
    line-height: 1.15;
    text-transform: uppercase;
  }
  .back-tagline {
    position: absolute;
    left: 0; right: 0; top: 215px;
    text-align: center;
    color: var(--white);
    font-size: 13px;
    letter-spacing: .5px;
  }
</style>
</head>
<body>
  <section class="card card--front">
    <div class="name-band"><span class="name-band__name">Marcus Hale</span></div>
    <div class="brand">Harborline Stay Collective</div>
    <div class="contact">
      <p class="contact__address">Po Box, 48 Harbor Row<br>Lakeview, ON 52110</p>
      <ul class="contact__list">
        <li class="contact__item">
          <svg class="contact__icon" viewBox="0 0 12 12"><rect x="3" y="0.5" width="6" height="11" rx="1" fill="none" stroke="var(--orange)" stroke-width="1.3"/></svg>
          555.204.7310
        </li>
        <li class="contact__item">
          <svg class="contact__icon" viewBox="0 0 12 12"><path d="M1 4c0-2 10-2 10 0v1H8V4H4v1H1z M2 6h8l1 5H1z" fill="var(--orange)"/></svg>
          +34 600 412 379
        </li>
        <li class="contact__item">
          <svg class="contact__icon" viewBox="0 0 12 12"><rect x="0.5" y="2" width="11" height="8" fill="var(--orange)"/><path d="M0.5 2l5.5 4.5L11.5 2" fill="none" stroke="var(--white)" stroke-width="1"/></svg>
          info@harborlinestaycollective.net
        </li>
        <li class="contact__item">
          <svg class="contact__icon" viewBox="0 0 12 12"><circle cx="6" cy="6" r="5.5" fill="var(--orange)"/><path d="M0.5 6h11M6 0.5c-3 3-3 8 0 11M6 0.5c3 3 3 8 0 11" fill="none" stroke="var(--white)" stroke-width=".8"/></svg>
          www.harborlinestaycollective.net
        </li>
      </ul>
    </div>
  </section>

  <section class="card card--back">
    <div class="back-brand">Harborline<br>Stay Collective</div>
    <p class="back-tagline">Luxury Hotel &amp; Resort Email Marketing</p>
  </section>
</body>
</html>
```